Stationary Package for Family Newsletter
The Hearth Gazette
Sunny & Cheer-packed
Renata K. Holloway
Advertising Sales Representative
P.O. Box 507369
Maplewood, TX 77490
rkholloway@thehearthgazette.example

```html
<!DOCTYPE html>
<html lang="en">
<head>
<meta charset="UTF-8">
<title>The Hearth Gazette – Business Card</title>
<link href="https://fonts.googleapis.com/css2?family=Roboto:ital,wght@0,400;0,700;0,900;1,900&display=swap" rel="stylesheet">
<style>
  :root {
    --backdrop: #d9d9d9;
    --card: #ffffff;
    --brand-red: #d8232a;
    --band-red: #e02a2f;
    --ink: #1c1c1c;
    --muted: #555555;
    --rule: #7a7a7a;
  }
  html, body {
    margin: 0;
    padding: 0;
    width: 1200px;
    height: 838px;
    overflow: hidden;
    background: var(--backdrop);
    font-family: "Roboto", Arial, sans-serif;
  }
  .card {
    position: absolute;
    left: 100px;
    top: 133px;
    width: 1000px;
    height: 571px;
    background: var(--card);
    box-shadow: 0 6px 24px rgba(0,0,0,0.18);
    overflow: hidden;
  }
  .masthead {
    position: absolute;
    left: 150px;
    top: 58px;
  }
  .masthead__name {
    margin: 0;
    color: var(--brand-red);
    font-weight: 900;
    font-size: 62px;
    letter-spacing: 0.5px;
    line-height: 1;
    text-transform: uppercase;
  }
  .masthead__tagline {
    margin: 8px 0 0 250px;
    color: var(--ink);
    font-weight: 900;
    font-style: italic;
    font-size: 28px;
    line-height: 1;
    white-space: nowrap;
  }
  .name-band {
    position: absolute;
    left: 0;
    top: 196px;
    width: 100%;
    height: 72px;
    background: var(--band-red);
  }
  .band-rule {
    position: absolute;
    left: 0;
    width: 100%;
    height: 3px;
    background: var(--rule);
  }
  .band-rule--upper { top: 274px; }
  .band-rule--lower { top: 474px; }
  .footer-band {
    position: absolute;
    left: 0;
    top: 483px;
    width: 100%;
    height: 44px;
    background: var(--band-red);
  }
  .person {
    position: absolute;
    left: 46px;
    top: 204px;
    color: #fff;
  }
  .person__name {
    margin: 0;
    font-weight: 700;
    font-size: 34px;
    line-height: 1.05;
  }
  .person__title {
    margin: 4px 0 0;
    font-size: 16px;
    font-weight: 400;
    opacity: 0.9;
  }
  .mailing {
    position: absolute;
    left: 46px;
    top: 300px;
    color: var(--muted);
    font-size: 22px;
    font-style: normal;
    line-height: 1.45;
  }
  .contact {
    position: absolute;
    left: 520px;
    top: 318px;
    margin: 0;
    padding: 0;
    list-style: none;
    color: var(--muted);
    font-size: 22px;
  }
  .contact__item {
    display: flex;
    align-items: center;
    gap: 12px;
    height: 38px;
  }
  .contact__icon {
    width: 22px;
    height: 22px;
    flex: none;
  }
</style>
</head>
<body>
  <main class="card">
    <header class="masthead">
      <h1 class="masthead__name">The Hearth Gazette</h1>
      <p class="masthead__tagline">Warm Stories Every Week!</p>
    </header>

    <div class="name-band"></div>
    <div class="band-rule band-rule--upper"></div>

    <section class="person">
      <h2 class="person__name">Renata K. Holloway</h2>
      <p class="person__title">Advertising Sales Representative</p>
    </section>

    <address class="mailing">
      P.O. Box 507369<br>
      Maplewood, TX 77490
    </address>

    <ul class="contact">
      <li class="contact__item">
        <svg class="contact__icon" viewBox="0 0 24 24" aria-hidden="true">
          <path fill="#d8232a" d="M6.6 2.5c.6-.3 1.3 0 1.6.6l1.6 3.4c.3.6.1 1.2-.4 1.6L8 9.3c.9 2.6 2.8 4.9 5.3 6.3l1.3-1.3c.5-.5 1.2-.6 1.7-.2l3.2 2c.6.4.8 1.1.5 1.7l-1 2.1c-.4.8-1.3 1.2-2.2 1C9.4 19.1 4.4 13.5 3.2 6.6c-.1-.9.3-1.8 1.1-2.3z"/>
        </svg>
        <span>: (713) 555-0142</span>
      </li>
      <li class="contact__item">
        <svg class="contact__icon" viewBox="0 0 24 24" aria-hidden="true">
          <rect x="3" y="9" width="18" height="11" rx="2" fill="#d8232a"/>
          <rect x="7" y="3" width="10" height="8" fill="#d8232a"/>
          <rect x="8.5" y="4.5" width="7" height="5" fill="#fff"/>
          <rect x="6" y="13" width="12" height="2" fill="#fff"/>
        </svg>
        <span>: (713) 555-0187</span>
      </li>
      <li class="contact__item">
        <svg class="contact__icon" viewBox="0 0 24 24" aria-hidden="true">
          <rect x="2" y="5" width="20" height="14" rx="2" fill="#d8232a"/>
          <path d="M3 6.5l9 6.5 9-6.5" fill="none" stroke="#fff" stroke-width="1.8"/>
        </svg>
        <span>rkholloway@thehearthgazette.example</span>
      </li>
    </ul>

    <div class="band-rule band-rule--lower"></div>
    <div class="footer-band"></div>
  </main>
</body>
</html>
```